Medical Company in need of Modern business card design for new Wound Care clinic.

Modern business card design for our Woundcare company. Logo and description of services can be found on our website; https://www.tovrel-woundcare.com/

```html
<!DOCTYPE html>
<html lang="en">
<head>
<meta charset="utf-8">
<title>Tovrel Woundcare – Business Card</title>
<link rel="stylesheet" href="https://fonts.googleapis.com/css2?family=Montserrat:wght@300;400;600&family=Roboto:wght@400&display=swap">
<style>
  :root {
    --bg: #3a322d;
    --card: #151515;
    --card-edge: #1d1d1d;
    --gold: #c9962e;
    --white: #f2f2f2;
    --rule: #6b6b6b;
    --pattern-a: #202020;
    --pattern-b: #2c2c2c;
  }
  * { box-sizing: border-box; margin: 0; padding: 0; }
  html, body { width: 1200px; height: 716px; overflow: hidden; }
  body {
    background: var(--bg);
    display: flex;
    align-items: center;
    justify-content: center;
    gap: 40px;
    font-family: "Roboto", sans-serif;
  }
  .card {
    width: 540px;
    height: 310px;
    background: var(--card);
    border-radius: 6px;
    position: relative;
    overflow: hidden;
    box-shadow: 0 10px 30px rgba(0,0,0,0.45);
  }

  /* Back side */
  .card-back__pattern {
    position: absolute;
    inset: 0;
    background: linear-gradient(135deg, var(--pattern-b) 0%, var(--pattern-a) 60%, var(--card) 100%);
  }
  .card-back__brand {
    position: absolute;
    left: 50%;
    top: 62%;
    transform: translate(-50%, -50%);
    font-family: "Montserrat", sans-serif;
    font-weight: 600;
    font-size: 26px;
    letter-spacing: 4px;
    color: var(--gold);
  }

  /* Front side */
  .card-front__brand {
    position: absolute;
    left: 36px;
    top: 96px;
    width: 250px;
    text-align: center;
    font-family: "Montserrat", sans-serif;
    font-weight: 300;
    font-size: 17px;
    letter-spacing: 5px;
    color: var(--gold);
    line-height: 1.5;
  }
  .card-front__divider {
    position: absolute;
    left: 304px;
    top: 60px;
    width: 1px;
    height: 120px;
    background: var(--rule);
  }
  .card-front__person {
    position: absolute;
    left: 322px;
    top: 62px;
  }
  .person__name {
    font-family: "Montserrat", sans-serif;
    font-weight: 600;
    font-size: 19px;
    color: var(--white);
    letter-spacing: 0.5px;
  }
  .person__title {
    font-family: "Roboto", sans-serif;
    font-size: 13px;
    color: var(--gold);
    margin-top: 2px;
  }
  .contact-list {
    list-style: none;
    margin-top: 14px;
  }
  .contact-list li {
    display: flex;
    align-items: center;
    gap: 7px;
    font-size: 11.5px;
    color: var(--white);
    margin-bottom: 6px;
  }
  .contact-list svg { width: 11px; height: 11px; flex: none; }
  .card-front__address {
    position: absolute;
    left: 36px;
    bottom: 40px;
    display: flex;
    align-items: center;
    gap: 7px;
    font-size: 12px;
    color: var(--white);
  }
  .card-front__address svg { width: 11px; height: 13px; }
</style>
</head>
<body>

  <section class="card card-back" aria-label="Card back">
    <div class="card-back__pattern" role="img" aria-label="Tonal repeating brand-mark pattern in silver and black"></div>
    <span class="card-back__brand">TOVREL</span>
  </section>

  <section class="card card-front" aria-label="Card front">
    <div class="card-front__brand">TOVREL<br>WOUNDCARE</div>
    <div class="card-front__divider"></div>

    <div class="card-front__person">
      <h1 class="person__name">DORIAN VAIL</h1>
      <p class="person__title">Founder &amp; CEO</p>
      <ul class="contact-list">
        <li>
          <svg viewBox="0 0 24 24" aria-hidden="true"><path fill="var(--gold)" d="M6.6 10.8a15.1 15.1 0 0 0 6.6 6.6l2.2-2.2a1 1 0 0 1 1-.25 11.4 11.4 0 0 0 3.6.57 1 1 0 0 1 1 1V20a1 1 0 0 1-1 1A17 17 0 0 1 3 4a1 1 0 0 1 1-1h3.5a1 1 0 0 1 1 1c0 1.25.2 2.45.57 3.57a1 1 0 0 1-.25 1z"/></svg>
          555-014-2290
        </li>
        <li>
          <svg viewBox="0 0 24 24" aria-hidden="true"><rect x="2" y="5" width="20" height="14" rx="1" fill="none" stroke="var(--gold)" stroke-width="2"/><path d="M2 6l10 7 10-7" fill="none" stroke="var(--gold)" stroke-width="2"/></svg>
          info@tovrel-woundcare.com
        </li>
        <li>
          <svg viewBox="0 0 24 24" aria-hidden="true"><g fill="none" stroke="var(--gold)" stroke-width="2"><circle cx="12" cy="12" r="10"/><ellipse cx="12" cy="12" rx="4" ry="10"/><path d="M2 12h20"/></g></svg>
          www.tovrel-woundcare.com
        </li>
      </ul>
    </div>

    <div class="card-front__address">
      <svg viewBox="0 0 20 26" aria-hidden="true"><path fill="var(--gold)" d="M10 0a10 10 0 0 0-10 10c0 7 10 16 10 16s10-9 10-16A10 10 0 0 0 10 0zm0 14a4 4 0 1 1 0-8 4 4 0 0 1 0 8z"/></svg>
      2180 Merrow Ln Ste 200 PMB 401772 Fairhaven, TX 75099
    </div>
  </section>

</body>
</html>
```